New Corporate website more focused on funnel and great design

Our company, Bold Harbor needs a new website to look like it's from 2021. We work with large businesses in the corporte world and need to reflect that we are professional, focused on our clients, and trsutworthy. It should include some/most of the components from our current site: boldharbor.com but should focus more about getting people to optin to out free downloads, which can be found on this page: https://www.boldharbor.com/get-started-with-a-prep-session/ and this page: https://www.boldharbor.com/team-onboarding/

Our new website should do a better job at explaining what we do, who we serve, and how we fix their problems of onboarding new leaders. Feel free to use dummy text if you are not sure what to put in for certain sections. I also would like to point out that most of the audiance is older, so we don't need anything too younge and flashy, or that is hard it use. it should have big clear fonts, plently of contrast, and work well for poeple who are not good at using the internet. Please use the colors of the logo, and you can add another color or two if you think it's fits

Industry/Entity Type

business consulting

Number of Pages Required

2 page

Font styles to use
Sans Serif

Requirements
Must have
• corporate feel, look professional, focus on getting new leads
Should not have
• cute or children feel

```html
<!DOCTYPE html>
<html lang="en">
<head>
<meta charset="utf-8">
<title>Bold Harbor — Accelerate business performance</title>
<link href="https://fonts.googleapis.com/css2?family=Lato:wght@400;700;900&display=swap" rel="stylesheet">
<style>
:root{
  --navy:#103f73;
  --blue:#1b5aa0;
  --blue-bright:#2a6fbd;
  --ink:#1d232b;
  --text:#4d5560;
  --muted:#8a929c;
  --line:#dfe4ea;
  --paper:#ffffff;
  --mist:#f4f6f9;
  --red:#d8403a;
  --green:#3a9b5c;
}
*{box-sizing:border-box;margin:0;padding:0}
html,body{width:1200px;height:4428px;overflow:hidden}
body{font-family:"Lato",Arial,sans-serif;color:var(--text);background:var(--paper);font-size:13px;line-height:1.55}
a{color:inherit;text-decoration:none}
.section{position:relative;width:1200px;overflow:hidden}
.brand{display:flex;align-items:center;gap:8px;font-weight:900;font-size:20px;color:var(--navy)}
.brand-mark{width:26px;height:26px;background:var(--navy)}
.btn{display:inline-block;background:var(--navy);color:#fff;font-weight:700;font-size:12px;padding:10px 20px;border-radius:2px}
.section-title{text-align:center;font-size:26px;font-weight:900;color:var(--ink)}
.underline{display:block;width:60px;height:3px;background:var(--blue);margin:10px auto 0}
.learn{font-size:11px;font-weight:700;color:var(--blue);letter-spacing:.5px}

.nav{height:60px;display:flex;align-items:center;justify-content:space-between;padding:0 140px 0 150px;border-bottom:1px solid var(--line)}
.nav-links{display:flex;gap:22px;font-size:12px;color:var(--ink);margin-left:auto;margin-right:26px}

.hero{height:480px;background:var(--paper)}
.hero-photo{position:absolute;left:300px;top:0;width:900px;height:440px;background:linear-gradient(90deg,#ffffff 0%,#e9ecef 18%,#b9bfc6 55%,#6b7078 100%)}
.hero-copy{position:absolute;left:150px;top:48px;width:520px}
.hero h1{font-size:30px;font-weight:900;color:var(--blue);line-height:1.2}
.hero h2{font-size:26px;font-weight:400;color:var(--ink);margin-top:4px}
.hero p{font-size:13px;color:var(--text);margin:16px 0 40px;width:360px}
.stat-card{position:absolute;left:400px;top:412px;width:400px;height:68px;background:#fff;box-shadow:0 6px 20px rgba(0,0,0,.15);display:flex;align-items:center;justify-content:center;gap:14px;border-left:3px solid var(--blue)}
.stat-card b{font-size:34px;font-weight:900;color:var(--blue)}
.stat-card span{font-size:15px;color:var(--ink)}

.effects{height:550px;padding-top:136px}
.effect-grid{display:flex;gap:60px;margin:52px 0 0 160px}
.effect{width:250px;border-left:3px solid var(--blue);padding-left:14px}
.effect h3{font-size:21px;font-weight:700;color:var(--blue);line-height:1.2}
.effect .kpi{font-size:14px;color:var(--ink);margin:6px 0 16px}
.effect p{font-size:12px;margin-bottom:14px}

.success{height:410px;padding:50px 0 0 150px;display:flex;gap:80px}
.success-copy{width:540px}
.success-copy h2{font-size:24px;font-weight:900;color:var(--ink)}
.success-copy h2 + i{display:block;width:50px;height:3px;background:var(--blue);margin:8px 0 18px}
.success-copy .lead{font-weight:700;color:var(--ink);margin-bottom:12px}
.success-copy p{font-size:12px;margin-bottom:12px}
.success-copy .link{color:var(--blue)}
.rates{width:260px}
.rates h3{font-size:17px;color:var(--ink);font-weight:700;margin-bottom:18px}
.rate{display:flex;align-items:center;gap:16px;margin-bottom:26px}
.rate b{font-size:44px;font-weight:900;color:var(--blue);line-height:1}
.rate small{display:block;font-size:11px;color:var(--muted)}
.rate svg{flex:none}

.testimonials{height:600px;background:var(--navy);color:#fff}
.testimonials .section-title{color:#fff;background:rgba(255,255,255,.08);padding:18px 0;margin-top:40px}
.quote-row{display:flex;gap:60px;margin:56px 0 0 155px}
.quote{width:190px}
.quote-head{display:flex;gap:10px;align-items:center;margin-bottom:14px}
.avatar{width:36px;height:36px;border-radius:50%;background:#8fa7c2;flex:none}
.quote-head b{font-size:13px;display:block}
.quote-head small{font-size:10px;color:#b7c7da}
.quote p{font-size:12px;color:#dbe4ee;background:rgba(255,255,255,.06);padding:12px;border-radius:2px}
.pager{position:absolute;left:0;right:0;top:520px;display:flex;justify-content:center;align-items:center;gap:14px;font-size:14px}
.dot{width:6px;height:6px;border-radius:50%;background:#6f8cb0}
.dot.on{background:#fff}

.clients{height:320px;padding-top:150px}
.clients .section-title em{font-style:normal;color:var(--blue);border-bottom:3px solid var(--blue)}
.logo-row{display:flex;justify-content:space-between;align-items:center;width:900px;margin:46px auto 0}
.client{display:flex;align-items:center;gap:8px;font-size:22px;font-weight:900;color:var(--ink)}
.client i{width:18px;height:18px;background:var(--blue)}

.contact{height:530px;background:linear-gradient(120deg,#3a3d42,#5b5f66 50%,#2f3236)}
.contact::before{content:"";position:absolute;inset:0;background:rgba(20,24,30,.45)}
.contact > *{position:relative}
.contact .section-title{color:#fff;padding-top:60px;font-size:24px}
.contact-grid{display:flex;gap:40px;margin:48px 0 0 150px}
.touch{width:250px;color:#e4e7eb;font-size:12px}
.touch h4{font-size:14px;color:#fff;margin-bottom:16px}
.touch p{margin-bottom:8px;display:flex;gap:8px;align-items:center}
.social{display:flex;gap:12px;margin-top:16px}
.social i{width:14px;height:14px;border-radius:50%;background:#fff}
.form{display:grid;grid-template-columns:200px 200px;gap:14px 16px}
.field{height:34px;background:#fff;font-size:11px;color:var(--muted);padding:9px 10px}
.message{width:200px;height:82px;grid-row:span 3;grid-column:2}
.submit{height:34px;background:var(--navy);color:#fff;font-size:12px;font-weight:700;display:flex;align-items:center;justify-content:center;width:200px}

.blog{height:530px;padding-top:70px}
.card-row{display:flex;gap:42px;margin:36px 0 0 150px}
.post{width:270px;box-shadow:0 3px 14px rgba(0,0,0,.1);background:#fff}
.post-img{height:140px;background:linear-gradient(135deg,#7b8590,#c8cdd3)}
.post-img.book{background:linear-gradient(135deg,#214e82,#6d8db2)}
.post-body{padding:12px 14px 16px}
.meta{display:flex;justify-content:space-between;font-size:10px;color:var(--muted);margin-bottom:6px}
.post h4{font-size:14px;color:var(--ink);line-height:1.3;margin-bottom:8px}
.post p{font-size:11px;margin-bottom:12px}

.prep{height:550px;background:var(--navy);color:#fff}
.prep .section-title{color:#fff;font-size:24px;padding-top:46px}
.prep-grid{display:flex;gap:56px;margin:60px 0 0 150px;align-items:flex-start}
.ebook{width:230px;height:250px;background:linear-gradient(160deg,#ffffff,#d9e2ec);border-radius:2px}
.prep-form{width:250px;display:flex;flex-direction:column;gap:14px;padding-top:10px}
.prep-form .btn{background:var(--blue-bright);text-align:center;padding:11px}
.prep-stats{width:230px}
.prep-stats b{font-size:46px;font-weight:900;line-height:1}
.prep-stats small{display:block;font-size:11px;color:#c4d2e3;margin:4px 0 22px}
.prep-stats a{font-size:11px;font-weight:700;border-bottom:1px solid #fff}

.footer{height:398px;padding:40px 0 0 150px;background:var(--mist)}
.footer-grid{display:flex;gap:80px}
.footer-about{width:230px;font-size:11px}
.footer-about p{margin:14px 0 18px}
.footer-col{width:150px}
.footer-col h5{font-size:12px;color:var(--ink);font-weight:900;margin-bottom:10px}
.footer-col a{display:block;font-size:11px;margin-bottom:5px}
.footer-col h5.gap{margin-top:20px}
.copyright{position:absolute;left:0;right:0;bottom:28px;text-align:center;font-size:10px;color:var(--muted);border-top:1px solid var(--line);padding-top:16px;margin:0 150px}
</style>
</head>
<body>

<header class="section nav">
  <a class="brand" href="#"><span class="brand-mark"></span>Bold Harbor</a>
  <nav class="nav-links"><a>Home</a><a>Who We Are</a><a>What We Do</a><a>Clients</a><a>Blog</a><a>Resources</a></nav>
  <a class="btn" href="#">Contact Us</a>
</header>

<section class="section hero">
  <div class="hero-photo" role="img" aria-label="Business leaders meeting around a laptop in an office"></div>
  <div class="hero-copy">
    <h1>Accelerate business performance</h1>
    <h2>During critical leadership transitions</h2>
    <p>Get there in 100 days what normally takes 6-12 months</p>
    <a class="btn" href="#">Contact Bold Harbor</a>
  </div>
  <div class="stat-card"><b>90%</b><span>of Bold Harbor Clients Succeed</span></div>
</section>

<section class="section effects">
  <h2 class="section-title">Common Effects after Transitions.<i class="underline"></i></h2>
  <div class="effect-grid">
    <article class="effect">
      <h3>Executive Onboarding</h3>
      <div class="kpi">40% of new leaders fail</div>
      <p>To help new leaders taking on new roles, the Bold Harbor Fast Start Roadmap process prepares leaders before the start, speeds up acceleration, sets direction, builds the team and sustains momentum.</p>
      <a class="learn" href="#">LEARN MORE ➔</a>
    </article>
    <article class="effect">
      <h3>Team Onboarding</h3>
      <div class="kpi">80% of M&amp;A fail to boost returns</div>
      <p>For leaders integrating teams post acquisition or re-organization, the Bold Harbor Fast Start Roadmap process gets all players on board with the change and accelerates achievement of cultural and business goals.</p>
      <a class="learn" href="#">LEARN MORE ➔</a>
    </article>
    <article class="effect">
      <h3>Acceleration &amp; Restart</h3>
      <div class="kpi">70% of transformations fall apart</div>
      <p>For executives leading through a strategic point of inflection or reinvigorating a stalled team, Bold Harbor programs deliver the tools to challenge, redirect a change process and deliver results that stick.</p>
      <a class="learn" href="#">LEARN MORE ➔</a>
    </article>
  </div>
</section>

<section class="section success">
  <div class="success-copy">
    <h2>Our Clients Success:-</h2><i></i>
    <p class="lead">Having a plan, a process and expert, hands-on support can mean the difference between success and failure.</p>
    <p>Our clients succeed in building cohesive teams, achieving their goals and creating lasting improvements in their businesses. <span class="link">Check out our case studies here.</span></p>
    <p>We’ve been able to reduce high-leader failure rates – 40% for leaders entering a new role, 70% for transformations and 80% for M&amp;A – to less than 10% for our clients. Our top 10 clients have used us over 180 times.</p>
    <p><span class="link">Learn more</span> about our clients, who compete in a wide range of industries, geographies, organization sizes and types, including private equity, middle market, major multi-global firms, high growth and not-for-profit.</p>
  </div>
  <aside class="rates">
    <h3>Failure Rates</h3>
    <div class="rate">
      <svg width="30" height="30" viewBox="0 0 30 30"><circle cx="15" cy="15" r="13" fill="none" stroke="var(--red)" stroke-width="2"/><path d="M10 10l10 10M20 10l-10 10" stroke="var(--red)" stroke-width="2.4"/></svg>
      <div><b>40%</b><small>Leaders entering a new role</small></div>
    </div>
    <div class="rate">
      <svg width="30" height="30" viewBox="0 0 30 30"><circle cx="15" cy="15" r="13" fill="none" stroke="var(--green)" stroke-width="2"/><path d="M9 15l4 4 8-8" fill="none" stroke="var(--green)" stroke-width="2.4"/></svg>
      <div><b>10%</b><small>Leaders who work with Bold Harbor</small></div>
    </div>
  </aside>
</section>

<section class="section testimonials">
  <h2 class="section-title">What our Clients Say</h2>
  <div class="quote-row">
    <figure class="quote">
      <div class="quote-head"><div class="avatar" role="img" aria-label="Client portrait"></div><div><b>Dana Whitfield,</b><small>CEO Software Integrated Solutions</small></div></div>
      <p>Somewhere right now, there is a first time CEO out there, not working with Bold Harbor, not following their Fast Start Roadmap, and we are worried for them.</p>
    </figure>
    <figure class="quote">
      <div class="quote-head"><div class="avatar" role="img" aria-label="Client portrait"></div><div><b>Dana Whitfield,</b><small>CEO Software Integrated Solutions</small></div></div>
      <p>Somewhere right now, there is a first time CEO out there, not working with Bold Harbor, not following their Fast Start Roadmap, and we are worried for them.</p>
    </figure>
    <figure class="quote">
      <div class="quote-head"><div class="avatar" role="img" aria-label="Client portrait"></div><div><b>Dana Whitfield,</b><small>CEO Software Integrated Solutions</small></div></div>
      <p>Somewhere right now, there is a first time CEO out there, not working with Bold Harbor, not following their Fast Start Roadmap, and we are worried for them.</p>
    </figure>
  </div>
  <div class="pager"><span>‹</span><i class="dot"></i><i class="dot on"></i><i class="dot"></i><span>›</span></div>
</section>

<section class="section clients">
  <h2 class="section-title">Our Top 10 Clients have used us <em>over 180 times</em></h2>
  <div class="logo-row">
    <span class="client">Northvale</span>
    <span class="client"><i></i>Crestline</span>
    <span class="client">Vantoria</span>
    <span class="client">Ironpeak</span>
    <span class="client"><i></i>Lumacore</span>
  </div>
</section>

<section class="section contact" role="img" aria-label="Office team at work, darkened background">
  <h2 class="section-title">Speak to one of our Partners Today</h2>
  <div class="contact-grid">
    <div class="touch">
      <h4>Get In Touch</h4>
      <p><svg width="12" height="12" viewBox="0 0 12 12"><path d="M3 1l2 2-1 2c1 1.5 1.5 2 3 3l2-1 2 2-1 2C5 11 1 7 1 2z" fill="#fff"/></svg>+1 212 555 0184</p>
      <p><svg width="12" height="12" viewBox="0 0 12 12"><path d="M3 1l2 2-1 2c1 1.5 1.5 2 3 3l2-1 2 2-1 2C5 11 1 7 1 2z" fill="#fff"/></svg>+1 646 555 0127</p>
      <div class="social"><i></i><i></i><i></i></div>
    </div>
    <div class="form">
      <div class="field">Name*</div>
      <div class="field message">Message</div>
      <div class="field">Phone*</div>
      <div class="field">Email Address*</div>
      <div></div>
      <div class="submit">Submit</div>
    </div>
  </div>
</section>

<section class="section blog">
  <h2 class="section-title">Featured books &amp; Blog Posts<i class="underline"></i></h2>
  <div class="card-row">
    <article class="post">
      <div class="post-img" role="img" aria-label="Executives at a press conference"></div>
      <div class="post-body"><div class="meta"><span>June 14, 2021</span><span>Executive Onboarding</span></div>
      <h4>Why Execs’s New CEO should Fail… Not now?</h4>
      <p>On the one hand, it looks like everything is stacked against her. Almost any set of assumptions plugged into our onboarding risk calculator suggests she…</p>
      <a class="learn">READ MORE ➔</a></div>
    </article>
    <article class="post">
      <div class="post-img book" role="img" aria-label="Cover of the Fast Start Roadmap book"></div>
      <div class="post-body"><div class="meta"><span>June 14, 2021</span><span>Books</span></div>
      <h4>Browse all our Books</h4>
      <a class="learn">READ MORE ➔</a></div>
    </article>
    <article class="post">
      <div class="post-img" role="img" aria-label="Historic black and white portrait of a statesman"></div>
      <div class="post-body"><div class="meta"><span>June 14, 2021</span><span>Leadership</span></div>
      <h4>Why “Thank You” Beats “No” In Strategic Selling</h4>
      <p>On the one hand, it looks like everything is stacked against her. Almost any set of assumptions plugged into our onboarding risk calculator suggests she…</p>
      <a class="learn">READ MORE ➔</a></div>
    </article>
  </div>
</section>

<section class="section prep">
  <h2 class="section-title">Get Started with the Prep session</h2>
  <div class="prep-grid">
    <div class="ebook" role="img" aria-label="Download cover: Fast Start Roadmap guide"></div>
    <div class="prep-form">
      <div class="field">First Name*</div>
      <div class="field">Last Name*</div>
      <div class="field">Phone Number*</div>
      <a class="btn">Download Now</a>
    </div>
    <div class="prep-stats">
      <b>95%</b><small>of our clients succeed</small>
      <b>30%</b><small>decrease in average failure rate</small>
      <a>READ MORE ABOUT IT HERE ➔</a>
    </div>
  </div>
</section>

<footer class="section footer">
  <div class="footer-grid">
    <div class="footer-about">
      <a class="brand"><span class="brand-mark"></span>Bold Harbor</a>
      <p>Lorem ipsum dolor sit amet, consectetur adipiscing elit, sed do eiusmod tempor incididunt ut labore et dolore magna.</p>
      <a class="btn">Contact Us</a>
    </div>
    <div class="footer-col">
      <h5>WHO WE ARE</h5><a>About</a><a>Team</a><a>In the News</a><a>Recent Events</a>
      <h5 class="gap">CLIENTS</h5><a>Onboarding</a><a>Transition Involvement</a>
    </div>
    <div class="footer-col">
      <h5>WHAT WE DO</h5><a>Executive Onboarding</a><a>Team Onboarding</a><a>Acceleration &amp; Restart</a><a>Case Studies</a>
      <h5 class="gap">RESOURCES</h5><a>Books</a><a>Podcast</a><a>Onboarding Tools</a>
    </div>
  </div>
  <div class="copyright">© 2021 Bold Harbor | BETTER RESULTS FASTER Since 2002</div>
</footer>

</body>
</html>
```